website refresh with jungle and/or gorilla theme for marketing agency

Our marketing agency needs a creative website boost. The website (which is Wordpress) is:https://www.tallmoosestudio.com. Given our name, we would like to have a jungle/gorilla theme. The Moose website should have a beastly presence. See the site now and how the gorilla is in your face. The text can remain the same, we just need a new layout and/or graphics. What other direction can I give? Not sure, we will know it when we see it.

Target Market(s)

small and medium sized businesses

Industry/Entity Type

Digital Marketing

Number of Pages Required

1 page

Colors

Designer to choose colors to be used in the design.

Requirements
Must have
• I don't really have any must have's. I don't want to limit the creativity of the designer.
Nice to have
• I am encouraging an out of the box design, something that isn't so "boxy" and traditional like the other sites.
Should not have
• I don't like standard looking sites that have a boxy layout with your standard cartoon and/or basic icons.

```html
<!DOCTYPE html>
<html lang="en">
<head>
<meta charset="utf-8">
<title>Moose Marketing</title>
<link href="https://fonts.googleapis.com/css2?family=Titillium+Web:wght@400;600;700;900&display=swap" rel="stylesheet">
<style>
:root{
  --teal:#1fb3a3;
  --teal-dark:#159a8b;
  --ink:#151515;
  --text:#4a4a4a;
  --muted:#8a8a8a;
  --white:#ffffff;
  --night:#0b0d0d;
  --line:#e3e3e3;
}
*{box-sizing:border-box;margin:0;padding:0}
html,body{width:1200px;height:3120px;overflow:hidden}
body{position:relative;background:var(--white);font-family:"Titillium Web",sans-serif;color:var(--text)}
.abs{position:absolute}
.hero{position:absolute;left:0;top:0;width:1200px;height:620px;background:radial-gradient(ellipse at 70% 40%,#3a3a38 0%,#1d1d1c 45%,#0c0c0c 100%)}
.hero-photo{position:absolute;inset:0}
.brand{position:absolute;left:94px;top:50px;color:var(--teal);font-weight:900;line-height:1}
.brand .name{font-size:34px;display:block}
.brand .tag{font-size:15px;color:var(--white);letter-spacing:1px;display:block;margin-top:2px;font-weight:700}
.main-nav{position:absolute;top:54px;left:700px;display:flex;gap:34px}
.main-nav a{color:var(--white);font-weight:700;font-size:12px;text-decoration:none;letter-spacing:.5px;padding-bottom:8px}
.main-nav a.active{border-bottom:2px solid var(--white)}
.hero-title{position:absolute;top:210px;left:0;width:1200px;text-align:center;color:var(--white);font-weight:900;font-size:60px;line-height:1.02;text-transform:uppercase;letter-spacing:1px}
.hero-title .hl{color:var(--teal)}
.hero-sub{position:absolute;top:345px;left:0;width:1200px;text-align:center;color:#e8e8e8;font-size:22px;line-height:1.5;text-transform:uppercase}
.btn-ghost{position:absolute;left:526px;top:443px;width:150px;height:38px;border:1.5px solid var(--teal);color:var(--teal);font-weight:700;font-size:13px;display:flex;align-items:center;justify-content:center;text-transform:uppercase}
.torn{position:absolute;left:0;top:575px}
.section-title{font-weight:900;font-size:38px;color:var(--ink);text-transform:uppercase;letter-spacing:.5px}
.section-sub{font-weight:700;font-size:18px;color:var(--teal);text-transform:uppercase;line-height:1.3}
.btn{background:var(--teal);color:var(--white);font-weight:700;font-size:13px;display:flex;align-items:center;justify-content:center;text-transform:uppercase}
.why-title{left:0;top:680px;width:1200px;text-align:center}
.why-sub{left:0;top:735px;width:1200px;text-align:center}
.video{left:212px;top:817px;width:406px;height:235px}
.why-copy{left:642px;top:818px;width:362px;font-size:13px;line-height:22px;color:#3c3c3c;font-weight:600}
.why-btn{left:642px;top:1000px;width:126px;height:34px}
.divider{left:0;top:1140px;width:1200px;height:10px;background:linear-gradient(#eee,#fff)}
.about-title{left:175px;top:1220px}
.about-sub{left:175px;top:1288px;width:430px;font-size:17px}
.about-copy{left:175px;top:1348px;width:450px;font-size:14px;line-height:24px;color:#3c3c3c;font-weight:600}
.perk{width:106px;height:134px;top:1525px;display:flex;flex-direction:column;align-items:flex-start;justify-content:center;color:var(--teal);font-weight:700;font-size:13px;line-height:1.1;text-transform:uppercase}
.perk svg{margin-bottom:8px}
.perk.on{background:var(--teal);color:var(--white);align-items:center;text-align:center}
.phones{left:722px;top:1242px;width:340px;height:418px}
.testimonials{left:0;top:1747px;width:1200px;height:442px;background:linear-gradient(180deg,#3dbcad 0%,#2cb2a2 60%,#38b7a8 100%)}
.t-title{left:0;top:1805px;width:1200px;text-align:center;color:var(--white);font-weight:900;font-size:36px;text-transform:uppercase}
.quote{background:var(--white);padding:26px 30px;font-style:italic;font-size:13px;line-height:22px;text-align:center;color:#3a3a3a;font-weight:600;overflow:hidden}
.quote.side{background:rgba(255,255,255,.35);color:rgba(255,255,255,.85)}
.avatar{width:52px;height:52px;border-radius:50%;background:linear-gradient(135deg,#6b6b6b,#3c3c3c)}
.t-name{color:var(--white);font-weight:700;font-size:13px;line-height:1.2}
.dots{left:550px;top:2147px;display:flex;gap:6px}
.dots span{width:8px;height:8px;border-radius:50%;background:var(--white)}
.brands-label{left:204px;top:2212px;font-weight:900;font-size:18px;color:var(--ink);line-height:1.15;text-transform:uppercase}
.partner{top:2225px;display:flex;align-items:center;gap:8px;font-weight:600;font-size:22px}
.rule{left:0;top:2288px;width:1200px;height:1px;background:var(--line)}
.contact-title{left:146px;top:2410px;font-size:50px;line-height:1;font-weight:900;color:var(--ink);text-transform:uppercase}
.contact-lead{left:146px;top:2535px;font-size:20px;line-height:32px;color:var(--muted);font-weight:700}
.contact-item{left:146px;display:flex;align-items:center;gap:26px;font-size:21px;color:#444}
.contact-item svg{width:22px;height:22px}
.form-card{left:649px;top:2371px;width:420px;height:464px;background:var(--white);box-shadow:0 2px 14px rgba(0,0,0,.12)}
.form-title{position:absolute;top:22px;left:0;width:100%;text-align:center;font-weight:900;font-size:30px;color:var(--ink);text-transform:uppercase}
.form-note{position:absolute;top:62px;left:0;width:100%;text-align:center;font-size:16px;color:var(--muted)}
.field{position:absolute;left:40px;width:340px;height:46px;border:1px solid #dcdcdc;border-radius:3px;font-size:16px;color:#777;padding:10px 14px}
.submit{position:absolute;left:143px;top:386px;width:237px;height:44px;font-size:15px}
.footer{left:0;top:2953px;width:1200px;height:167px;background:linear-gradient(180deg,#0d1010,#151a19)}
.f-col{top:2980px;color:var(--white);font-size:11px;line-height:17px;font-weight:700}
.f-col h4{color:var(--teal);font-size:13px;margin-bottom:2px}
</style>
</head>
<body>
<header class="hero">
  <div class="hero-photo" role="img" aria-label="Close-up photograph of a gorilla's face in low light"></div>
  <div class="brand"><span class="name">MOOSE</span><span class="tag">MARKETING</span></div>
  <nav class="main-nav">
    <a class="active">HOME</a><a>ABOUT</a><a>LEARN</a><a>PORTFOLIO</a><a>CONTACT</a>
  </nav>
  <h1 class="hero-title"><span class="hl">Friendly</span> and Searchly<br>Marketing Beasts</h1>
  <p class="hero-sub">Get performancedriven digital marketing<br>leaders on your team</p>
  <div class="btn-ghost">Get in touch</div>
</header>
<svg class="torn" width="1200" height="50" viewBox="0 0 1200 50" aria-hidden="true">
  <path fill="#fff" d="M0 30 L40 22 L70 31 L110 20 L150 28 L190 18 L230 27 L270 21 L310 30 L350 19 L400 26 L440 17 L480 25 L520 20 L560 29 L600 18 L650 24 L690 16 L730 26 L780 19 L820 28 L860 17 L900 25 L950 20 L990 29 L1030 18 L1080 27 L1120 19 L1160 26 L1200 21 L1200 50 L0 50 Z"/>
</svg>

<h2 class="abs section-title why-title">Why Moose Marketing?</h2>
<p class="abs section-sub why-sub">Moose Marketing is the apex predator of the Friendly<br>and Searchly marketing industries.</p>
<div class="abs video" role="img" aria-label="Laptop showing a teal-tinted intro video of a team member, with a play button" style="background:linear-gradient(180deg,#2bb5a5 0%,#1e9f90 88%,#cfcfcf 88%,#bdbdbd 100%)">
  <svg class="abs" style="left:181px;top:90px" width="44" height="44" viewBox="0 0 44 44"><circle cx="22" cy="22" r="20" fill="none" stroke="#fff" stroke-width="2"/><path d="M18 14 L30 22 L18 30 Z" fill="#fff"/></svg>
</div>
<p class="abs why-copy">We are senior marketing experts with the skills to create revenue-producing marketing funnels. In this age of big data, there is no better way to earn instant visibility with your audience than to have a REAL team of skilled pros on your side. Is your marketing funnel maximizing revenue and conversions? Learn the single biggest mistake companies make in their marketing funnel and how to fix it.</p>
<div class="abs btn why-btn">More videos</div>

<div class="abs divider"></div>

<h2 class="abs section-title about-title">About Us</h2>
<p class="abs section-sub about-sub">What sets us apart from other marketin agencies is our team of A-players.</p>
<p class="abs about-copy">Each team member has proven themselves to be in the top 1% of all marketers. They are the 1 percenters who are passionate about what they do and have proven experience to back up their incredible skill sets.<br>Led by Daniel Hartwell, who has built and sold 4 companies himself and written 5 books (one best-seller), the team at Moose Marketing specializes in user acquisition, lead generation, and brand visibility.</p>
<div class="abs perk" style="left:175px">
  <svg width="40" height="40" viewBox="0 0 40 40" fill="none" stroke="currentColor" stroke-width="2"><path d="M4 36h32M8 36V26M16 36V20M24 36V14M32 36V8M6 20L18 10l6 4 10-10"/></svg>
  More<br>traffic
</div>
<div class="abs perk on" style="left:262px">
  <svg width="40" height="40" viewBox="0 0 40 40" fill="none" stroke="currentColor" stroke-width="2"><circle cx="20" cy="15" r="10"/><circle cx="20" cy="15" r="5"/><path d="M13 23l-4 13 5-3 3 4 3-9M27 23l4 13-5-3-3 4-3-9"/></svg>
  Higher<br>quality<br>leds
</div>
<div class="abs perk" style="left:418px">
  <svg width="40" height="40" viewBox="0 0 40 40" fill="none" stroke="currentColor" stroke-width="2"><circle cx="24" cy="12" r="8"/><path d="M24 8v8M2 30h8l6-4h8a3 3 0 010 6h-8M24 32l10-6a3 3 0 013 4l-11 8H2"/></svg>
  More<br>sales
</div>
<div class="abs phones" role="img" aria-label="Two smartphones displaying a photo of a team meeting around a table" style="background:linear-gradient(135deg,#3a3a3a,#5a5f5c 40%,#8a8d86 60%,#444 100%);border-radius:22px"></div>

<section class="abs testimonials" role="img" aria-label="Teal-tinted forest background"></section>
<h2 class="abs t-title">Testimonials</h2>
<div class="abs quote side" style="left:-130px;top:1890px;width:360px;height:128px;text-align:right">Lorem ipsum dolor sit amet. Aenean commodo ligula eget dolor natoque penatibus et magnis dis nec quam felis, ultricies nec, pellentesque eu. Nulla consequa.</div>
<div class="abs quote" style="left:333px;top:1886px;width:527px;height:136px">Lorem ipsum dolor sit amet, consectetuer adipiscing elit. Aenean commodo ligula eget dolor. Aenean massa. Cum sociis natoque penatibus et magnis dis parturient montes, nascetur ridiculus mus. Donec quam felis, ultricies nec, pellentesque eu, pretium quis, sem. Nulla consequa.</div>
<div class="abs quote side" style="left:948px;top:1890px;width:360px;height:128px;text-align:left">Lorem ipsum dolor sit amet, consectetuer ligula eget dolor. Aenean massa. Cum parturient montes, nascetur ridiculus mus. Donec pellentesque eu, pretium.</div>
<div class="abs avatar" role="img" aria-label="Client portrait" style="left:492px;top:2050px"></div>
<p class="abs t-name" style="left:564px;top:2060px">Sam Ridley, CEO<br>Company Name</p>
<div class="abs avatar" role="img" aria-label="Client portrait" style="left:1113px;top:2050px;opacity:.7"></div>
<p class="abs t-name" style="left:0;top:2072px;opacity:.6">, CEO</p>
<div class="abs dots"><span></span><span></span><span></span><span></span><span></span></div>

<p class="abs brands-label">Name brands<br>we've worked with</p>
<div class="abs partner" style="left:448px;color:#3a3a3a"><svg width="22" height="22"><circle cx="11" cy="11" r="9" fill="#8bc34a"/></svg>Northline</div>
<div class="abs partner" style="left:668px;color:#b3262d;font-size:18px">Cotterell Brands</div>
<div class="abs partner" style="left:850px;color:#1f3f8a;font-size:20px"><svg width="20" height="20"><rect width="18" height="18" fill="#f0a92a"/></svg>Harborview</div>
<div class="abs rule"></div>

<h2 class="abs contact-title">Get in touch<br>with us</h2>
<p class="abs contact-lead">First appointment for free!<br>You can also call us with number below</p>
<div class="abs contact-item" style="top:2628px">
  <svg viewBox="0 0 24 24"><path fill="#1fb3a3" d="M12 2a7 7 0 00-7 7c0 5 7 13 7 13s7-8 7-13a7 7 0 00-7-7zm0 9.5A2.5 2.5 0 1112 6.5a2.5 2.5 0 010 5z"/></svg>17470 N Your full address here
</div>
<div class="abs contact-item" style="top:2673px">
  <svg viewBox="0 0 24 24" fill="none" stroke="#1fb3a3" stroke-width="2"><rect x="2" y="5" width="20" height="14"/><path d="M2 5l10 8 10-8"/></svg>support@Moose.com
</div>
<div class="abs contact-item" style="top:2718px">
  <svg viewBox="0 0 24 24"><path fill="#1fb3a3" d="M6.6 10.8a15 15 0 006.6 6.6l2.2-2.2a1 1 0 011-.25 11.4 11.4 0 003.6.57 1 1 0 011 1V20a1 1 0 01-1 1A17 17 0 013 4a1 1 0 011-1h3.5a1 1 0 011 1c0 1.25.2 2.45.57 3.57a1 1 0 01-.25 1z"/></svg>(555) 347 - 0148
</div>

<form class="abs form-card">
  <h3 class="form-title">Appointment form</h3>
  <p class="form-note">It only takes few seconds</p>
  <div class="field" style="top:118px">Name</div>
  <div class="field" style="top:182px">Email Address</div>
  <div class="field" style="top:246px;height:114px">Your Question</div>
  <div class="btn submit">Request an appointment</div>
</form>

<footer class="abs footer" role="img" aria-label="Dark jungle foliage background"></footer>
<div class="abs brand" style="left:188px;top:2985px"><span class="name">MOOSE</span><span class="tag">MARKETING</span></div>
<div class="abs f-col" style="left:392px"><h4>Navigation</h4>How it Works<br>Pricing Page<br>Try Our Tools<br>Sign Up<br>Login</div>
<div class="abs f-col" style="left:560px"><h4>Policy</h4>Conditions &amp; Terms<br>About us<br>Privacy Policy<br>Write to us<br>Block Security</div>
<div class="abs f-col" style="left:752px"><h4>Contacts</h4>Your Street Adress<br>Phone Numbers<br>Email Addresses<br>Working Hours<br>Products</div>
<div class="abs f-col" style="left:938px"><h4>Social</h4>Friendly<br>Searchly+<br>Chirper</div>
</body>
</html>
```